Mondeko Ltd

I have been recommended by my web builder to get a fully designed website from two different companies such as yourselves. I have 5 products initially and need a site with world wide appeal.

Target Market(s)

Care Home and Nail Bar Industry

Industry/Entity Type

Builder

Number of Pages Required

5+ page

Font styles to use
Sans Serif

Colors

Designer to choose colors to be used in the design.

Requirements
Must have
• Great Innovative Home Page
Nice to have
• I would like the background moving as in clouds rushing past. Similar to the way car lights are speeded up in night time ads. I have vel-tor quality shots of various cloud formations that I can send
Should not have
• Usual boring design

```html
<!DOCTYPE html>
<html lang="en">
<head>
<meta charset="utf-8">
<title>Mondeko Ltd — Nail Bar &amp; Care Home</title>
<link rel="stylesheet" href="https://fonts.googleapis.com/css2?family=Open+Sans:wght@300;400;600;700&family=Playfair+Display:wght@400&family=Noto+Serif:wght@400&display=swap">
<style>
  :root {
    --backdrop: #f5ece8;
    --paper: #ffffff;
    --brand-blue: #1589c9;
    --accent-cyan: #9fe0f0;
    --accent-orange: #f5a623;
    --ink: #222222;
    --ink-soft: #555555;
    --tile: #f7ede9;
    --badge: #666666;
    --rule: #bbbbbb;
    --footer: #151515;
  }
  * { margin: 0; padding: 0; box-sizing: border-box; }
  html, body { width: 686px; height: 1200px; overflow: hidden; background: var(--backdrop); }
  body { font-family: "Open Sans", Arial, sans-serif; color: var(--ink); }
  .canvas { position: relative; width: 686px; height: 1200px; overflow: hidden; }
  .sheet { position: absolute; left: 76px; top: 0; width: 536px; height: 1200px; background: var(--paper); }
  .abs { position: absolute; }

  /* header */
  .phone-btn { left: 86px; top: 25px; width: 83px; height: 22px; background: var(--brand-blue); color: #fff;
    font-size: 7.5px; display: flex; align-items: center; gap: 7px; padding-left: 9px; }
  .brand { left: 292px; top: 24px; width: 100px; text-align: center; font-size: 17px; font-weight: 600;
    color: var(--brand-blue); letter-spacing: 0.5px; }
  .hours { left: 408px; top: 30px; font-size: 7.5px; color: var(--accent-orange); }
  .social { display: flex; gap: 5px; align-items: center; }
  .social span { width: 6px; height: 6px; border-radius: 50%; background: currentColor; display: block; }
  .social.top { left: 542px; top: 31px; color: #333; }
  .double-rule { left: 86px; top: 72px; width: 513px; height: 3px; border-top: 1px solid #333; border-bottom: 1px solid #333; }
  .main-nav { top: 84px; left: 0; width: 686px; height: 12px; }
  .main-nav a, .footer-nav a { position: absolute; transform: translateX(-50%); text-decoration: none;
    font-size: 8px; font-weight: 600; color: var(--ink); white-space: nowrap; }

  /* hero */
  .hero { left: 86px; top: 102px; width: 513px; height: 220px;
    background: linear-gradient(100deg, #b08660 0%, #6b5140 30%, #8b8b8b 55%, #a9a9a9 100%); }
  .hero-title { right: 112px; top: 150px; text-align: right; color: #fff; font-weight: 300;
    font-size: 29px; line-height: 40px; }
  .hero-btn { left: 379px; top: 242px; width: 154px; height: 36px; border: 1px solid var(--accent-cyan);
    color: var(--accent-cyan); font-size: 8px; letter-spacing: 1.5px; display: flex; align-items: center; justify-content: center; }
  .hero-next { left: 582px; top: 198px; color: #fff; font-size: 20px; font-weight: 300; }

  /* section headings */
  .heading { font-family: "Playfair Display", Georgia, serif; font-weight: 400; font-size: 22px; color: var(--ink); line-height: 1.1; }
  .subheading { font-size: 13px; color: var(--brand-blue); }
  .btn { background: var(--brand-blue); color: #fff; display: flex; align-items: center; justify-content: center; }

  .about-text { left: 89px; top: 395px; width: 328px; font-family: "Noto Serif", Georgia, serif;
    font-size: 8.3px; line-height: 14.4px; color: var(--ink-soft); text-indent: 26px; }
  .find-btn { left: 86px; top: 485px; width: 80px; height: 23px; font-size: 7.5px; letter-spacing: 0.6px; }

  .service-list { left: 438px; top: 395px; width: 159px; list-style: none; background: var(--tile); }
  .service-list li { height: 22.4px; display: flex; justify-content: space-between; align-items: center;
    padding: 0 14px 0 12px; font-size: 6px; font-weight: 700; letter-spacing: 1px; color: #333;
    border-bottom: 1px solid #fff; }
  .service-list li b { color: var(--brand-blue); font-weight: 400; font-size: 8px; }

  /* posts */
  .center-col { left: 0; width: 686px; text-align: center; }
  .post { top: 574px; width: 164px; text-align: center; }
  .post-photo { height: 100px; }
  .post-date { display: inline-block; margin-top: 20px; width: 62px; height: 11px; background: var(--badge);
    color: #fff; font-size: 7px; line-height: 11px; }
  .post-title { margin-top: 14px; font-family: "Noto Serif", Georgia, serif; font-size: 12px; line-height: 17.5px; color: #333; }
  .post-meta { margin-top: 9px; font-size: 7px; display: flex; justify-content: center; gap: 4px; align-items: center; }
  .more-posts { left: 301px; top: 798px; font-size: 10px; font-weight: 700; letter-spacing: 1.4px; display: flex; align-items: center; gap: 6px; }
  .section-rule { left: 86px; top: 829px; width: 513px; height: 1px; background: var(--rule); }

  /* care home */
  .care-title { left: 90px; top: 846px; font-size: 23px; line-height: 26.5px; }
  .care-text { left: 88px; top: 925px; width: 285px; font-size: 10.3px; line-height: 14.6px; color: var(--ink-soft); }
  .learn-btn { left: 86px; top: 1030px; width: 80px; height: 24px; font-size: 10px; font-weight: 600; }
  .care-photo { left: 410px; top: 852px; width: 189px; height: 207px;
    background: linear-gradient(160deg, #9aa868 0%, #c8cfa0 45%, #4f90b8 100%); }

  /* footer */
  .site-footer { left: 86px; top: 1086px; width: 513px; height: 114px; background: var(--footer); }
  .footer-brand { left: 0; top: 1104px; width: 686px; text-align: center; color: #fff; font-size: 14px; font-weight: 600; letter-spacing: 0.5px; }
  .footer-nav { top: 1146px; left: 0; width: 686px; }
  .footer-nav a { color: #fff; font-size: 7px; font-weight: 400; }
  .social.bottom { left: 316px; top: 1166px; color: #fff; }
  .copyright { left: 0; top: 1180px; width: 686px; text-align: center; color: #ddd; font-size: 7.5px; }
</style>
</head>
<body>
<div class="canvas">
  <div class="sheet"></div>

  <header>
    <div class="abs phone-btn">
      <svg width="9" height="9" viewBox="0 0 24 24" aria-hidden="true"><path fill="#fff" d="M6.6 10.8a15 15 0 0 0 6.6 6.6l2.2-2.2c.3-.3.7-.4 1-.2 1.1.4 2.3.6 3.6.6.6 0 1 .4 1 1V20c0 .6-.4 1-1 1A17 17 0 0 1 3 4c0-.6.4-1 1-1h3.5c.6 0 1 .4 1 1 0 1.3.2 2.5.6 3.6.1.3 0 .7-.2 1z"/></svg>
      555-014-2290
    </div>
    <div class="abs brand">Mondeko</div>
    <div class="abs hours">Open: Mn - Sn 8am - 10PM</div>
    <div class="abs social top" aria-label="Social links"><span></span><span></span><span></span><span></span><span></span></div>
    <div class="abs double-rule"></div>
    <nav class="abs main-nav">
      <a style="left:183px">HOME</a><a style="left:245px">ABOUT US</a><a style="left:313px">SERVICES</a>
      <a style="left:378px">GALLERY</a><a style="left:435px">BLOG</a><a style="left:494px">CONTACT</a>
    </nav>
  </header>

  <section>
    <div class="abs hero" role="img" aria-label="Portrait of a model with red lips and dark manicured nails"></div>
    <h1 class="abs hero-title">Lorem ipsum dolor<br>sit amet consec</h1>
    <div class="abs hero-btn">MACKE AN APPOINTMENT</div>
    <div class="abs hero-next">›</div>
  </section>

  <section>
    <h2 class="abs heading" style="left:89px;top:338px">Welcome!</h2>
    <div class="abs subheading" style="left:88px;top:363px">About us</div>
    <p class="abs about-text">Our Nail Bar opened its doors, with a team of talented, passionate, caring, creative people dedicated to doing great nails and giving our clients amazing experiences. We are always looking for the best, most natural products we can find. When you walk into our doors, you will be greeted with a smile and taken care of by everyone on our team. Every moment of your visit should be enjoyable and relaxed.</p>
    <div class="abs btn find-btn">FIND OUT MORE</div>

    <h2 class="abs heading" style="left:438px;top:338px">Our Services</h2>
    <div class="abs subheading" style="left:438px;top:363px">Out offer</div>
    <ul class="abs service-list">
      <li>MANICURES <b>&gt;</b></li><li>INTUITIVE SERVICES <b>&gt;</b></li><li>PEDICURES <b>&gt;</b></li>
      <li>MASSAGES <b>&gt;</b></li><li>NAILS <b>&gt;</b></li>
    </ul>
  </section>

  <section>
    <h2 class="abs heading center-col" style="top:523px">Latest Posts</h2>
    <div class="abs subheading center-col" style="top:547px">Blog updates</div>

    <article class="abs post" style="left:86px">
      <div class="post-photo" role="img" aria-label="Hands with brightly coloured painted nails" style="background:linear-gradient(135deg,#f2c6b4,#e8506a 50%,#f0a070)"></div>
      <span class="post-date">MAR 3,17</span>
      <h3 class="post-title" style="font-weight:400">Ultra Glam Gold Nail Polishes for Holiday.</h3>
      <div class="post-meta">💬 0 <span style="color:var(--accent-orange)">♥</span> 10</div>
    </article>
    <article class="abs post" style="left:262px">
      <div class="post-photo" role="img" aria-label="Pedicured feet with orchid flowers" style="background:linear-gradient(135deg,#efe4e6,#e6c2b0 55%,#f4eef0)"></div>
      <span class="post-date">MAR 3,17</span>
      <h3 class="post-title" style="font-weight:400">Ultra Glam Gold Nail Polishes for Holiday.</h3>
      <div class="post-meta">💬 0 <span style="color:var(--accent-orange)">♥</span> 10</div>
    </article>
    <article class="abs post" style="left:436px">
      <div class="post-photo" role="img" aria-label="Red polka dot nail art on a hand" style="background:linear-gradient(135deg,#c81a20,#e8b8a4 55%,#b51218)"></div>
      <span class="post-date">MAR 3,17</span>
      <h3 class="post-title" style="font-weight:400">Ultra Glam Gold Nail Polishes for Holiday.</h3>
      <div class="post-meta">💬 0 <span style="color:var(--accent-orange)">♥</span> 10</div>
    </article>

    <div class="abs more-posts">MORE POSTS
      <svg width="18" height="8" viewBox="0 0 18 8" aria-hidden="true"><path d="M0 4h13" stroke="#1589c9" stroke-width="2"/><path d="M11 0l7 4-7 4z" fill="#1589c9"/></svg>
    </div>
    <div class="abs section-rule"></div>
  </section>

  <section>
    <h2 class="abs heading care-title">Our outher service<br>Care Home</h2>
    <p class="abs care-text">Lorem ipsum dolor sit amet, consectetur adipiscing elit. Fusce et lacus sit amet eros consequat congue eget eget metus. Interdum et malesuada fames ac ante ipsum primis in faucibus. Nunc eu viverra ex. Donec aliquam mi maximus mi interdum, eget tristique lacus pulvinar.</p>
    <div class="abs btn learn-btn">Learn More</div>
    <div class="abs care-photo" role="img" aria-label="Carer smiling with an elderly resident outdoors"></div>
  </section>

  <footer>
    <div class="abs site-footer"></div>
    <div class="abs footer-brand">Mondeko</div>
    <nav class="abs footer-nav">
      <a style="left:203px">HOME</a><a style="left:258px">ABOUT US</a><a style="left:317px">SERVICES</a>
      <a style="left:374px">GALLERY</a><a style="left:424px">BLOG</a><a style="left:476px">CONTACT</a>
    </nav>
    <div class="abs social bottom" aria-label="Social links"><span></span><span></span><span></span><span></span><span></span></div>
    <div class="abs copyright">© 2016 All Rights Reserved</div>
  </footer>
</div>
</body>
</html>
```